Redesign Home Page

We need a new home page with a white background. Our company provides singing instruction to students world wide, both in person and on line. We're looking for a very clean and open design with maximum white space. The main goal of the page will be to get users to sign up for our mailing list. The current site is www.kelvarsong.com. I think the new page can be a long page (scrolll down is ok), to allow for more white space while still using the text from the current page.
Updates

Project Deadline Extended
Reason: Hello to all Designers, I apologize for not giving feedback this weekend. We went out of town for the Memorial Day holiday and I had no internet. I will be extending the deadline to Thursday. -Marcus

Target Market(s)

Singers of all ages and abilities, especially beginners.

Industry/Entity Type

It Company

Requirements
Must have
• 1. A white background
2. Lots of open space
3. An email sign up form on the top right that reads:
a. “Improve Your Singing Now.
b. Sign up for our Free Video Series: Tone Pathway
4. Testimonails: found on https://www.kelvarsong.com/tone-ascent
5. My logo with the piano
6. My photo
7. Learn about our Lessons in:
a. San Francisco
b. Alameda
8. On Line Programs:
a. Tone Ascent
b. Zelvo Lessons

Nice to have
• Link to current student page: http://kelvarsong.com/what-students-say/students2
Pictures of singers
Video box: Use Marcus_Example
Should not have
• See "KelvarSong Redesign" file for more details.

```html
<!DOCTYPE html>
<html lang="en">
<head>
<meta charset="utf-8">
<title>Marcus Kelvar – Home</title>
<link rel="stylesheet" href="https://fonts.googleapis.com/css2?family=Roboto+Condensed:wght@300;400&family=Open+Sans:wght@400;600&family=Gelasio:ital@1&display=swap">
<style>
:root{
  --blue:#0a6ebd;
  --blue-dark:#07589a;
  --blue-input:#0a5795;
  --orange:#f07c22;
  --header:#3f3f3f;
  --header-active:#2f2f2f;
  --ink:#333;
  --muted:#777;
  --rule:#cfcfcf;
  --quote-bg:#f3f3f3;
  --white:#fff;
}
*{margin:0;padding:0;box-sizing:border-box}
html,body{width:1053px;height:1200px;overflow:hidden;background:var(--white)}
body{position:relative;font-family:"Open Sans",Arial,sans-serif;color:var(--ink)}
.abs{position:absolute}
.heading{font-family:"Roboto Condensed",Arial,sans-serif;font-weight:300;color:var(--ink)}
.body-text{font-size:11px;line-height:17px;color:var(--muted)}
.btn{position:absolute;display:flex;align-items:center;justify-content:center;color:var(--white);font-family:"Roboto Condensed",Arial,sans-serif;text-decoration:none}
.btn-blue{background:var(--blue)}
.btn-orange{background:var(--orange)}

/* header */
.site-header{position:absolute;left:0;top:0;width:1053px;height:67px;background:linear-gradient(#474747,#393939)}
.brand{position:absolute;left:164px;top:20px;display:flex;align-items:center;gap:8px;color:var(--white);font-family:"Roboto Condensed",Arial,sans-serif;font-size:22px;font-weight:400}
.brand-dot{width:18px;height:18px;border-radius:50%;background:var(--blue)}
.nav a{position:absolute;top:29px;font-size:12px;color:var(--white);text-decoration:none;font-family:"Roboto Condensed",Arial,sans-serif;letter-spacing:.2px}
.nav-active{position:absolute;left:411px;top:0;width:56px;height:67px;background:var(--header-active);border-top:3px solid var(--blue)}

/* hero */
.hero{position:absolute;left:0;top:67px;width:1053px;height:280px;background:linear-gradient(90deg,#e4e4e4,#f1f1f1 45%,#dedede)}
.coach-photo{position:absolute;left:200px;top:6px;width:247px;height:274px;background:linear-gradient(#d9d9d9,#2a2a2a 45%,#161616)}
.hero-title{left:449px;top:117px;font-size:17px;font-weight:400}
.hero-title .accent{color:var(--blue)}
.hero-underline{left:796px;top:132px}
.hero-text{left:449px;top:159px;width:450px}
.hero-link{left:451px;top:201px;font-size:13.5px;color:var(--blue)}

/* video */
.video-box{left:164px;top:375px;width:156px;height:128px;background:#e2e2e2}
.section-title{font-size:18px}
.accent{color:var(--blue)}

.rule-h{position:absolute;left:0;width:1053px;border-top:1px dashed var(--rule)}
.rule-v{position:absolute;left:527px;top:531px;height:165px;border-left:1px dashed var(--rule)}

.blog-link{left:541px;top:577px;font-size:12px;font-weight:600;color:var(--blue)}
.pager{position:absolute;top:555px;width:12px;height:13px}

/* testimonials */
.avatar{left:227px;top:781px;width:88px;height:88px;border-radius:50%;background:radial-gradient(#8a6a5a,#2b211d);border:3px solid var(--white);box-shadow:0 0 0 1px #ddd}
.person-name{left:200px;top:874px;width:142px;text-align:center;font-size:11.5px;font-weight:600;color:var(--blue)}
.person-place{left:200px;top:887px;width:142px;text-align:center;font-size:11px;color:var(--muted)}
.quote{left:340px;top:784px;width:487px;height:113px;background:var(--quote-bg);border-left:4px solid var(--blue);padding:26px 18px 0;font-family:"Gelasio",Georgia,serif;font-style:italic;font-size:11.5px;line-height:17px;color:#555;text-align:center}

/* footer */
.site-footer{position:absolute;left:0;top:947px;width:1053px;height:224px;background:var(--blue);color:var(--white)}
.footer-bar{position:absolute;left:0;top:1171px;width:1053px;height:29px;background:var(--blue-dark);color:var(--white);font-size:11px;text-align:center;line-height:29px}
.footer-title{position:absolute;top:27px;font-family:"Roboto Condensed",Arial,sans-serif;font-size:15px;color:var(--white)}
.footer-list{position:absolute;top:61px;list-style:none;font-size:11px;line-height:18.3px}
.footer-text{position:absolute;left:469px;top:60px;width:210px;font-size:11px;line-height:17px}
.email-field{position:absolute;left:469px;top:106px;width:208px;height:30px;background:var(--blue-input);font-size:10px;padding:9px 8px;color:#e6eef7}
.social{position:absolute;left:721px;display:flex;align-items:center;gap:10px;font-size:11.5px;font-weight:600}
.social-dot{width:20px;height:20px;border-radius:50%;background:#e8eef5}
</style>
</head>
<body>

<header class="site-header">
  <div class="brand"><span class="brand-dot"></span>Marcus Kelvar</div>
  <div class="nav-active"></div>
  <nav class="nav">
    <a style="left:424px">HOME</a>
    <a style="left:485px">LESSONS</a>
    <a style="left:560px">OUR SERVICES</a>
    <a style="left:660px">OUR BLOG</a>
    <a style="left:744px">CONTACT US</a>
    <a style="left:837px">LOGIN</a>
  </nav>
</header>

<section class="hero">
  <div class="coach-photo" role="img" aria-label="Portrait of vocal coach Marcus in a black turtleneck"></div>
</section>
<h1 class="abs heading hero-title">Improve your singing with <span class="accent">Professional Vocal Coach Marcus D.Kelvar</span></h1>
<svg class="abs hero-underline" width="90" height="10" viewBox="0 0 90 10"><path d="M2 7 Q45 1 88 4" fill="none" stroke="#444" stroke-width="1.2"/></svg>
<p class="abs body-text hero-text">This is Draftboard's version &nbsp;of Lorem Ipsum. Proin gravida nibh vel velit auctor aliqu ddum auctor, t auctor aliquet. Aenean sollicitudin, loremum auctor,</p>
<p class="abs heading hero-link">Sign up for our Free Video Series ( Tone Pathway ) &amp; Many More Online Lessons</p>
<a class="btn btn-orange" style="left:449px;top:235px;width:116px;height:34px;font-size:14px">Get Started Now</a>

<div class="abs video-box">
  <svg width="156" height="128" viewBox="0 0 156 128"><circle cx="78" cy="64" r="27" fill="none" stroke="#8db8dc" stroke-width="2"/><path d="M70 51 L90 64 L70 77 Z" fill="#8db8dc"/></svg>
</div>
<h2 class="abs heading section-title" style="left:349px;top:375px">Subscribe To Our New Online Training Series <span class="accent">( Tone Ascent )</span></h2>
<p class="abs body-text" style="left:351px;top:405px;width:540px">This is Draftboard's version &nbsp;of Lorem Ipsum. Proin gravida nibh vel velit auctor aliquet.sollicitudin, lorem quis bibendum auctor, nisi elit consequat ipsum, nec sagittis sem nibh id elit. Duis sed odio sit amet nibh vulputate cursus a sit amet mauris. Morbi accumsan ipsum velit.</p>
<a class="btn btn-blue" style="left:351px;top:467px;width:90px;height:33px;font-size:14px">Get Started</a>

<div class="rule-h" style="top:531px"></div>
<div class="rule-v"></div>
<div class="rule-h" style="top:696px"></div>

<h2 class="abs heading section-title" style="left:164px;top:550px">Free Consultation With Marcus</h2>
<p class="abs body-text" style="left:164px;top:579px;width:350px">This is Draftboard's version &nbsp;of Lorem Ipsum. Proin gravida nibh veli velit auctor aliquet.sollicitudin, lorem quis bibendum auctor, nisi elit consequat ipsum, nec sagittis sem nibh.</p>
<a class="btn btn-blue" style="left:164px;top:644px;width:188px;height:33px;font-size:14px">Book Your Free Consultation</a>

<h2 class="abs heading section-title" style="left:541px;top:550px">Latest From Our Blog</h2>
<svg class="pager" style="left:861px" viewBox="0 0 12 13"><rect width="12" height="13" fill="#d6d6d6"/><path d="M7.5 3 L4 6.5 L7.5 10" fill="none" stroke="#fff" stroke-width="1.5"/></svg>
<svg class="pager" style="left:875px" viewBox="0 0 12 13"><rect width="12" height="13" fill="#0a6ebd"/><path d="M4.5 3 L8 6.5 L4.5 10" fill="none" stroke="#fff" stroke-width="1.5"/></svg>
<p class="abs blog-link">How Voice Transformation Works</p>
<p class="abs body-text" style="left:541px;top:597px;width:350px">This is Draftboard's version &nbsp;of Lorem Ipsum. Proin gravida nibh veli velit auctor aliquet.sollicitudin, lorem quis bibendum auctor, nisi elit consequat ipsum, nec sagittis sem nibh.</p>
<a class="btn btn-blue" style="left:541px;top:655px;width:72px;height:25px;font-size:11.5px">Read More</a>

<h2 class="abs heading section-title" style="left:0;top:721px;width:1053px;text-align:center">See What People Are Saying About Us</h2>
<div class="abs" style="left:480px;top:754px;width:96px;border-top:2px dotted #666"></div>

<svg class="abs" style="left:140px;top:832px" width="12" height="20" viewBox="0 0 12 20"><path d="M10 1 L2 10 L10 19" fill="none" stroke="#999" stroke-width="1.5"/></svg>
<svg class="abs" style="left:901px;top:832px" width="12" height="20" viewBox="0 0 12 20"><path d="M2 1 L10 10 L2 19" fill="none" stroke="#999" stroke-width="1.5"/></svg>

<div class="abs avatar" role="img" aria-label="Photo of student Renata Holloway"></div>
<p class="abs person-name">Renata Holloway</p>
<p class="abs person-place">Washington DC</p>
<svg class="abs" style="left:332px;top:834px" width="8" height="12" viewBox="0 0 8 12"><path d="M8 0 L0 6 L8 12 Z" fill="#0a6ebd"/></svg>
<blockquote class="abs quote">This is Draftboard's version &nbsp;of Lorem Ipsum. Proin gravida nibh vel velit aliquet Aenea sollicitudin, lorem quis bibendum auctor, nisi elit consequat ipsum, nec sagittis sem nibh id elit. Duis sed odio sit amet. nisi elit consequat ipsum,is sed odio sit amet.</blockquote>

<footer class="site-footer">
  <h3 class="footer-title" style="left:216px">QUICK LINKS</h3>
  <ul class="footer-list" style="left:216px"><li>Home</li><li>About Us</li><li>Our Services</li><li>Lessons</li><li>Our Blog</li><li>Contact Us</li></ul>
  <ul class="footer-list" style="left:333px"><li>Login</li><li>Signup</li><li>FAQ's</li><li>Terms &amp; Conditions</li><li>Privacy Policy</li><li>Sitemap</li></ul>
  <h3 class="footer-title" style="left:469px">NEWSLETTER</h3>
  <p class="footer-text">Subscribe to our newslette to get latest updates right into ypur inbox.</p>
  <div class="email-field">Enter your email address...</div>
  <a class="btn btn-orange" style="left:469px;top:144px;width:74px;height:29px;font-size:12.5px">Submit</a>
  <h3 class="footer-title" style="left:721px">NEWSLETTER</h3>
  <div class="social" style="top:60px"><span class="social-dot"></span>Circlepage</div>
  <div class="social" style="top:92px"><span class="social-dot"></span>Chirpline</div>
  <div class="social" style="top:124px"><span class="social-dot"></span>Worknet</div>
  <div class="social" style="top:156px"><span class="social-dot"></span>Clipstream</div>
</footer>
<div class="footer-bar">Copyright 2014 - All Rights Reserved</div>

</body>
</html>
```